Striking Business Card for Exotic Car Ministry

Design a striking business card that will motivate people to go to the website. I want this card to be unique but readable. We use exotic cars to minister to people on Vidgrove as well as car shows. I would like the background to be black and high impact.

This is the craziest thing, a minimum of 300 words? How do you make something so simple, so difficult to complete? I guess I will just continue to type until I get the necessary three hundred words. No, not even close now, so I continue typing. Christmas is nearing and may be here before I achieve this silly goal of three hundred words. They may as well ask for one thousand words as it would be similarly insane. It would even be helpful to know my word count.

Target Market(s)

Men

Industry/Entity Type

Automotive

Contact Information for Business Card

Logo with Ministry & Outreach nearby to describe service. Include Wrenlark42.com and Morris@Wrenlark42.com somewhere on card. Bullet points: Vidgrove, Car Shows, Forum, Outreach...Include: Watch Videos on Vidgrove logo.

On the rear of the card: Commit your work to the Lord, and your plans will succeed. Proverbs 16:3

There will be no telephone number. Include image of 2017 Corvane TLR on the front.

Colors

Designer to choose colors to be used in the design.

Requirements
Must have
• Card should be a dark color like black or gray. Must not be a traditional boring card.
Nice to have
• I think this describes it well.
Should not have
• I wouldnt expect any questions.

```html
<!DOCTYPE html>
<html lang="en">
<head>
<meta charset="utf-8">
<title>Wrenlark Business Card</title>
<link href="https://fonts.googleapis.com/css2?family=Oswald:wght@400;600;700&display=swap" rel="stylesheet">
<style>
  :root {
    --backdrop: #2a2c30;
    --card-black: #0b0b0c;
    --ink-white: #f4f4f4;
    --brand-red: #e0141c;
    --deep-red: #7a0a0e;
    --stripe-red: #b3151b;
    --stripe-dark: #5c0a0d;
  }
  * { margin: 0; padding: 0; box-sizing: border-box; }
  html, body {
    width: 1200px; height: 1000px; overflow: hidden;
    background: var(--backdrop);
    font-family: "Oswald", "Arial Narrow", sans-serif;
  }
  .canvas { position: relative; width: 1200px; height: 1000px; }
  .card {
    position: absolute; left: 280px; width: 640px; height: 366px;
    border-radius: 22px; overflow: hidden; background: var(--card-black);
    box-shadow: 0 14px 30px rgba(0,0,0,.55);
  }
  .card--photo { top: 70px; }
  .card--contact { top: 560px; }
  .card svg.card-art { position: absolute; inset: 0; width: 100%; height: 100%; }

  .brand-name {
    position: absolute; font-weight: 700; color: var(--ink-white);
    text-transform: uppercase; letter-spacing: 3px; line-height: 1;
  }

  /* photo side */
  .photo-area { position: absolute; inset: 0; }
  .site-top {
    position: absolute; top: 22px; right: 30px; font-weight: 600; font-size: 17px;
    color: var(--ink-white); letter-spacing: 1px; text-transform: uppercase;
  }
  .site-top .accent { color: var(--brand-red); }
  .card--photo .brand-name { left: 150px; top: 228px; font-size: 46px; }
  .verse {
    position: absolute; left: 24px; bottom: 22px; font-weight: 600; font-size: 13.5px;
    color: var(--ink-white); text-transform: uppercase; letter-spacing: .4px;
  }
  .verse .ref { color: var(--brand-red); }

  /* contact side */
  .card--contact .brand-name { left: 160px; top: 140px; font-size: 62px; }
  .contact-line {
    position: absolute; display: flex; align-items: center; gap: 8px;
    font-weight: 600; font-size: 14px; color: var(--ink-white);
    text-transform: uppercase; letter-spacing: .5px;
  }
  .contact-line svg { width: 14px; height: 14px; flex: none; }
  .contact-line .accent { color: var(--brand-red); }
  .contact-web { left: 28px; top: 26px; }
  .contact-mail { left: 28px; top: 52px; }
  .watch-videos { right: 28px; bottom: 24px; font-size: 15px; }
  .channel-dot { width: 14px; height: 14px; border-radius: 50%; background: var(--brand-red); }
</style>
</head>
<body>
<main class="canvas">

  <section class="card card--photo">
    <svg class="card-art" viewBox="0 0 640 366" aria-hidden="true">
      <defs>
        <linearGradient id="photoTone" x1="0" y1="0" x2="1" y2="1">
          <stop offset="0" stop-color="#3a0507"/>
          <stop offset=".5" stop-color="#b5141b"/>
          <stop offset="1" stop-color="#4a0608"/>
        </linearGradient>
      </defs>
      <polygon points="0,0 640,0 640,366 548,366 0,138" fill="url(#photoTone)"/>
      <line x1="0" y1="138" x2="548" y2="366" stroke="var(--brand-red)" stroke-width="3"/>
    </svg>
    <div class="photo-area" role="img" aria-label="Red-toned photo of a 2017 Corvane TLR supercar speeding along a road with motion blur"></div>
    <p class="site-top">www.<span class="accent">wrenlark42</span>.com</p>
    <p class="brand-name">Wrenlark</p>
    <p class="verse">Commit your work to the Lord, and your plans will succeed. <span class="ref">Proverbs 16:3</span></p>
  </section>

  <section class="card card--contact">
    <svg class="card-art" viewBox="0 0 640 366" aria-hidden="true">
      <polygon points="120,366 420,0 520,0 220,366" fill="var(--stripe-dark)"/>
      <polygon points="150,366 450,0 490,0 190,366" fill="var(--stripe-red)"/>
      <polygon points="260,366 560,0 600,0 300,366" fill="var(--stripe-dark)" opacity=".7"/>
    </svg>
    <p class="brand-name">Wrenlark</p>
    <p class="contact-line contact-web">
      <svg viewBox="0 0 14 14" aria-hidden="true"><circle cx="7" cy="7" r="6" fill="none" stroke="#e0141c" stroke-width="1.5"/><ellipse cx="7" cy="7" rx="2.6" ry="6" fill="none" stroke="#e0141c" stroke-width="1.2"/><line x1="1" y1="7" x2="13" y2="7" stroke="#e0141c" stroke-width="1.2"/></svg>
      www.<span class="accent">wrenlark42</span>.com
    </p>
    <p class="contact-line contact-mail">
      <svg viewBox="0 0 14 14" aria-hidden="true"><rect x="1" y="3" width="12" height="8" rx="1" fill="#e0141c"/><polyline points="1.5,3.5 7,8 12.5,3.5" fill="none" stroke="#0b0b0c" stroke-width="1.2"/></svg>
      Morris@Wrenlark42.com
    </p>
    <p class="contact-line watch-videos">Watch videos on <span class="channel-dot"></span> Vidgrove</p>
  </section>

</main>
</body>
</html>
```